Kneadwell Haven Business Card Design

I want to create a very elegant and sophisticated two sided business card for my massage practice (www.kneadwellhaven-example.com). I have attached the logo and a PDF with some ideas down for the back of the card but I am open to suggestions. I will want to tie in a post card and flyer to the card later.
Similar colors to website would be great.
Target Market(s)
High end clientele, people looking for a sophisticated spa experience.
Industry/Entity Type
Massage
Contact Information for Business Card
Kneadwell Haven
7218 Larchmont Blvd S, Suite 305
Alderbrook, OR 97999
(555) 340-7816
www.kneadwellhaven-example.com

```html
<!DOCTYPE html>
<html lang="en">
<head>
<meta charset="utf-8">
<title>Kneadwell Haven Business Card</title>
<link rel="stylesheet" href="https://fonts.googleapis.com/css2?family=Cinzel:wght@500&family=Arimo:wght@400&display=swap">
<style>
  :root {
    --backdrop: #111111;
    --cream: #e4dfd3;
    --teal: #1c3643;
    --ink: #1e3a47;
    --line-light: rgba(228, 223, 211, 0.7);
  }
  html, body {
    margin: 0;
    width: 1200px;
    height: 1000px;
    overflow: hidden;
    background: var(--backdrop);
  }
  .canvas {
    position: relative;
    width: 1200px;
    height: 1000px;
  }
  .card {
    position: absolute;
    width: 520px;
    height: 300px;
    border-radius: 24px;
    box-sizing: border-box;
  }
  .card-front {
    left: 50px;
    top: 220px;
    background: var(--cream);
    display: flex;
    align-items: center;
    justify-content: center;
  }
  .brand-name {
    font-family: "Cinzel", serif;
    font-weight: 500;
    font-size: 34px;
    letter-spacing: 1px;
    color: var(--ink);
    text-transform: uppercase;
  }
  .card-back {
    left: 630px;
    top: 480px;
    background: var(--teal);
    color: var(--cream);
    font-family: "Arimo", sans-serif;
  }
  .holder {
    position: absolute;
    left: 40px;
    top: 118px;
    width: 190px;
    text-align: center;
  }
  .holder-name {
    font-size: 17px;
    letter-spacing: 0.5px;
  }
  .holder-role {
    font-size: 13px;
    margin-top: 2px;
  }
  .divider {
    position: absolute;
    left: 252px;
    top: 50px;
    width: 1px;
    height: 200px;
    background: var(--line-light);
  }
  .contact {
    position: absolute;
    left: 272px;
    top: 58px;
    width: 230px;
    text-align: center;
  }
  .contact-name {
    font-family: "Cinzel", serif;
    font-weight: 500;
    font-size: 15px;
    letter-spacing: 1px;
    text-transform: uppercase;
    margin-bottom: 12px;
  }
  .contact-rule {
    height: 1px;
    background: var(--line-light);
    margin: 8px 10px;
  }
  .contact-line {
    font-size: 13px;
    line-height: 19px;
  }
</style>
</head>
<body>
<main class="canvas">
  <section class="card card-front" aria-label="Card front">
    <div class="brand-name">Kneadwell Haven</div>
  </section>

  <section class="card card-back" aria-label="Card back">
    <div class="holder">
      <div class="holder-name">LOREM IPSUM</div>
      <div class="holder-role">owner</div>
    </div>
    <div class="divider"></div>
    <div class="contact">
      <div class="contact-name">Kneadwell Haven</div>
      <div class="contact-rule"></div>
      <div class="contact-line">7218 Larchmont Blvd S, Suite 305</div>
      <div class="contact-line">Alderbrook, OR 97999</div>
      <div class="contact-line">(555) 340-7816</div>
      <div class="contact-rule"></div>
      <div class="contact-line">www.kneadwellhaven-example.com</div>
    </div>
  </section>
</main>
</body>
</html>
```